Attorney Business Card

I need a business card that looks professional yet modern. I am an Attorney. , I need a professional yet modern business card for my law practice. My logo and information have been uploaded. , I need a business card that looks professional yet modern. I am an Attorney. , I need a professional yet modern business card for my law practice. My logo and information have been uploaded.

Industry/Entity Type

Business

Requirements
Must have
• My logo which has been uploaded , my logo , My logo which has been uploaded , my logo

```html
<!DOCTYPE html>
<html lang="en">
<head>
<meta charset="utf-8">
<title>Marendale Law Firm – Business Card</title>
<link rel="stylesheet" href="https://fonts.googleapis.com/css2?family=Open+Sans:wght@300;400;600;800&display=swap">
<style>
  :root {
    --card-bg: #e4e4e4;
    --accent-blue: #03a9ec;
    --ink-dark: #4d4d4d;
    --icon-ink: #454545;
  }
  html, body {
    margin: 0;
    padding: 0;
    width: 1200px;
    height: 720px;
    overflow: hidden;
    background: var(--card-bg);
  }
  .card {
    position: relative;
    width: 1200px;
    height: 720px;
    background: var(--card-bg);
    font-family: "Open Sans", Arial, sans-serif;
    color: var(--ink-dark);
    overflow: hidden;
  }
  .card-graphics {
    position: absolute;
    inset: 0;
  }
  .firm-mark {
    position: absolute;
    left: 122px;
    top: 290px;
    width: 400px;
    text-align: center;
    color: var(--accent-blue);
    font-weight: 600;
    font-size: 40px;
    line-height: 1.15;
    letter-spacing: 3px;
    text-transform: uppercase;
    margin: 0;
  }
  .attorney-name {
    position: absolute;
    left: 70px;
    top: 416px;
    margin: 0;
    font-weight: 800;
    font-size: 45px;
    letter-spacing: -1.6px;
    color: var(--ink-dark);
    white-space: nowrap;
  }
  .attorney-title {
    position: absolute;
    left: 71px;
    top: 474px;
    margin: 0;
    font-weight: 300;
    font-size: 30px;
    letter-spacing: 13.4px;
    color: var(--ink-dark);
    white-space: nowrap;
  }
  .contact-list {
    position: absolute;
    left: 800px;
    top: 0;
    margin: 0;
    padding: 0;
    list-style: none;
    font-size: 22px;
    color: var(--ink-dark);
  }
  .contact-item {
    position: absolute;
    left: 0;
    white-space: nowrap;
    letter-spacing: 1px;
  }
  .contact-address {
    top: 304px;
    font-size: 23px;
    line-height: 29px;
    letter-spacing: 4.2px;
    text-transform: uppercase;
  }
  .contact-mobile { top: 420px; }
  .contact-phone  { top: 481px; }
  .contact-fax    { top: 538px; }
  .contact-email  { top: 591px; left: 4px; text-transform: uppercase; }
  .contact-web    { top: 645px; left: 4px; text-transform: uppercase; }
</style>
</head>
<body>
<div class="card">
  <svg class="card-graphics" width="1200" height="720" viewBox="0 0 1200 720" aria-hidden="true">
    <!-- accent bands -->
    <rect class="accent-band-top" x="522" y="0" width="58" height="417" fill="var(--accent-blue)"/>
    <rect class="accent-band-contact" x="718" y="303" width="57" height="417" fill="var(--accent-blue)"/>

    <!-- firm mark circle -->
    <circle class="firm-mark-dot" cx="322" cy="222" r="46" fill="none" stroke="var(--accent-blue)" stroke-width="4"/>

    <!-- icons -->
    <g class="contact-icons" fill="var(--icon-ink)" stroke="none">
      <!-- home -->
      <path class="icon-home" d="M746 313 L770 334 L764 334 L764 354 L752 354 L752 342 L740 342 L740 354 L728 354 L728 334 L722 334 Z"/>
      <!-- mobile -->
      <rect class="icon-mobile" x="733" y="413" width="26" height="46" rx="3" fill="none" stroke="var(--icon-ink)" stroke-width="3"/>
      <rect x="737" y="419" width="18" height="31" fill="none" stroke="var(--icon-ink)" stroke-width="1.5"/>
      <circle cx="746" cy="454" r="1.8"/>
      <!-- phone handset -->
      <path class="icon-phone" d="M727 479 C724 482 723 487 726 494 C731 505 740 514 752 520 C759 523 764 522 767 518 L770 514 C771 512 770 510 768 509 L760 504 C758 503 756 503 755 505 L752 508 C746 505 740 499 737 493 L740 490 C742 489 742 487 741 485 L736 477 C735 475 732 474 731 476 Z"/>
      <!-- printer -->
      <g class="icon-printer">
        <rect x="734" y="537" width="24" height="11"/>
        <rect x="724" y="548" width="44" height="18" rx="3"/>
        <rect x="733" y="559" width="26" height="17" fill="var(--accent-blue)" stroke="var(--icon-ink)" stroke-width="3"/>
        <rect x="738" y="565" width="16" height="2"/>
        <rect x="738" y="570" width="16" height="2"/>
      </g>
      <!-- at sign -->
      <g class="icon-at" fill="none" stroke="var(--icon-ink)" stroke-width="4">
        <circle cx="747" cy="609" r="8"/>
        <path d="M755 601 L755 613 C755 618 759 620 762 619 C766 617 767 613 767 608 A20 19 0 1 0 756 626"/>
      </g>
      <!-- globe -->
      <g class="icon-globe" fill="none" stroke="var(--icon-ink)" stroke-width="3">
        <circle cx="747" cy="662" r="19"/>
        <ellipse cx="747" cy="662" rx="8" ry="19"/>
        <line x1="728" y1="662" x2="766" y2="662"/>
        <path d="M731 652 H763 M731 672 H763"/>
      </g>
    </g>
  </svg>

  <p class="firm-mark">Marendale<br>Law Firm</p>

  <h1 class="attorney-name">DANIEL MARENDALE, ESQ.</h1>
  <p class="attorney-title">ATTORNEY AT LAW</p>

  <ul class="contact-list">
    <li class="contact-item contact-address">2180 Cedarline Ave.<br>Penthouse<br>Westbrook, CA 90480</li>
    <li class="contact-item contact-mobile">555.210.4471</li>
    <li class="contact-item contact-phone">555.318.6020</li>
    <li class="contact-item contact-fax">555.318.6020</li>
    <li class="contact-item contact-email">daniel@mdlawgroup.com</li>
    <li class="contact-item contact-web">www.mdlawgroup.com</li>
  </ul>
</div>
</body>
</html>
```